Calvoterra business card

a nice business card with the logo,
Calvoterra
Teresa Lindqvist
Marketing Director
CH-1563 Geneva
Switzerland
+41 76 382 1904
email: Teresa.Lindqvist@calvoterra-mail.example

Target Market(s)

fertilizer business people, very nice and classic business card, normal size, make it nice and funky, try to make it different from the normal boring ones if possible.

Industry/Entity Type

Farming

Number of Pages Required

1 page

Requirements
Must have
• logo, Calvoterra, my name - mail and phone number
regular business card size for me to print easy please

```html
<!DOCTYPE html>
<html lang="en">
<head>
<meta charset="utf-8">
<title>Calvoterra business card</title>
<link rel="stylesheet" href="https://fonts.googleapis.com/css2?family=Carlito:wght@400;700&display=swap">
<style>
  :root {
    --paper: #ffffff;
    --ink-grey: #97a3a1;
    --lime: #a6ff0a;
    --edge: #3a3a3a;
    --white: #ffffff;
  }
  * { margin: 0; padding: 0; box-sizing: border-box; }
  html, body {
    width: 1200px;
    height: 1200px;
    overflow: hidden;
    background: var(--paper);
    font-family: "Carlito", "Calibri", sans-serif;
  }
  .sheet { position: relative; width: 1200px; height: 1200px; }

  .card {
    position: absolute;
    left: 250px;
    width: 700px;
    height: 400px;
  }
  .card--front {
    top: 133px;
    background: var(--paper);
    border: 1px solid var(--edge);
    color: var(--ink-grey);
  }
  .card--back {
    top: 667px;
    background: var(--lime);
    color: var(--white);
  }

  .holder { position: absolute; left: 61px; top: 48px; }
  .holder__name {
    font-size: 48px;
    font-weight: 400;
    line-height: 1;
    letter-spacing: 0.2px;
  }
  .holder__first { font-weight: 700; }
  .holder__role {
    font-size: 22px;
    line-height: 1;
    margin-top: 6px;
  }

  .contact {
    position: absolute;
    left: 61px;
    top: 259px;
    list-style: none;
    font-size: 22px;
    line-height: 30px;
  }

  .brand-mark {
    position: absolute;
    left: 470px;
    top: 110px;
    width: 180px;
    display: flex;
    flex-direction: column;
    align-items: center;
    gap: 18px;
  }
  .brand-mark__dot {
    width: 110px;
    height: 110px;
    border-radius: 50%;
    background: var(--lime);
  }
  .brand-mark__name {
    font-size: 26px;
    font-weight: 700;
    color: var(--lime);
  }

  .back-brand {
    position: absolute;
    left: 0;
    top: 55px;
    width: 100%;
    display: flex;
    flex-direction: column;
    align-items: center;
  }
  .back-brand__dot {
    width: 120px;
    height: 120px;
    border-radius: 50%;
    background: var(--white);
  }
  .back-brand__name {
    margin-top: 100px;
    font-size: 17px;
    font-weight: 700;
    letter-spacing: 0.62em;
    padding-left: 0.62em;
    text-transform: uppercase;
    line-height: 1;
  }
  .address {
    position: absolute;
    left: 0;
    top: 344px;
    width: 100%;
    text-align: center;
    font-size: 23px;
    line-height: 1;
    white-space: pre;
  }
</style>
</head>
<body>
<main class="sheet">
  <section class="card card--front" aria-label="Business card front">
    <header class="holder">
      <h1 class="holder__name"><span class="holder__first">teresa</span> lindqvist</h1>
      <p class="holder__role">marketing director</p>
    </header>
    <ul class="contact">
      <li>+41 76 382 1904</li>
      <li>teresa.lindqvist@calvoterra-mail.example</li>
      <li>www.calvoterra.example</li>
    </ul>
    <div class="brand-mark">
      <span class="brand-mark__dot" aria-hidden="true"></span>
      <span class="brand-mark__name">calvoterra</span>
    </div>
  </section>

  <section class="card card--back" aria-label="Business card back">
    <div class="back-brand">
      <span class="back-brand__dot" aria-hidden="true"></span>
      <span class="back-brand__name">Calvoterra</span>
    </div>
    <p class="address">calvoterra  //  ch-1563 geneva  //  switzerland</p>
  </section>
</main>
</body>
</html>
```